Professional website for psychological services

Create a professional, easy to navigate website using soothing coastal images and incorporate company logo in design. Website is for a small private clinic that provides psychological services and must be appealing to professional men and women. A website I really like is www.velmorlodge.example I would love something like similar.

Target Market(s)

Professional men and women seeking psychological services

Industry/Entity Type

Mental Health

Number of Pages Required

5+ page

Requirements
Must have
• The website must incorporate the logo provided. The name of the company/website is Brindle Oak Wellness Aftercare. Colors must compliment the logo, must be coastal and soothing yet very professional. I would like a website like www.velmorlodge.example
• Pages will be:Home, Services, FAQ and Contact Us. The images included of the building and office are for the contact us page. Under the tab Servies: Individual Psychotherapy, Family Therapy, EMDR I will provide specific content for each.
Nice to have
• I want the website to be easy to navigate and the font easy to read. The writing on the logo is very light and I'm open to changing it slightly if it will be better aesthetically.
Should not have
• Please no pictures of any swimsuits, alcoholic beverages, etc. This is a professional psychological clinic.

```html
<!DOCTYPE html>
<html lang="en">
<head>
<meta charset="utf-8">
<title>Brindle Oak Wellness Aftercare</title>
<link rel="stylesheet" href="https://fonts.googleapis.com/css2?family=Source+Sans+3:wght@300;400;600&display=swap">
<style>
:root{
  --teal:#14aacb;
  --teal-dark:#0e9dbd;
  --ink:#1d1d1d;
  --text:#444b50;
  --white:#ffffff;
  --pale:#f2fafc;
  --footer:#eceff3;
  --line:#cfd6da;
}
*{box-sizing:border-box;margin:0;padding:0}
html,body{width:1200px;height:2628px;overflow:hidden}
body{position:relative;background:var(--white);font-family:"Source Sans 3",sans-serif;color:var(--text)}
.abs{position:absolute}

/* header */
.site-header{left:0;top:0;width:1200px;height:96px;background:var(--white)}
.brand{left:149px;top:26px;display:flex;align-items:center;gap:8px}
.brand-dot{width:16px;height:16px;border-radius:50%;background:var(--teal)}
.brand-name{font-size:17px;font-weight:400;color:var(--teal);line-height:1.1;width:130px}
.main-nav{left:470px;top:36px;display:flex;align-items:center;font-size:14px;color:var(--ink)}
.main-nav a{color:var(--ink);text-decoration:none;padding:0 34px}
.main-nav a.active{color:var(--teal)}
.main-nav .sep{color:var(--ink)}
.btn{display:flex;align-items:center;justify-content:center;font-size:12px;letter-spacing:.3px;text-transform:uppercase;text-decoration:none}
.btn-solid{background:var(--teal);color:var(--white)}
.header-cta{left:892px;top:35px;width:157px;height:28px}

/* hero */
.hero-photo{left:0;top:96px;width:1200px;height:456px;background:linear-gradient(180deg,#c9def0 0%,#a7c3d8 28%,#7d8f7a 45%,#5b7fa0 60%,#4a6f95 100%)}
.hero-card{left:559px;top:312px;width:490px;height:264px;background:var(--teal);color:var(--white);text-align:center}
.hero-title{position:absolute;left:0;right:0;top:40px;font-size:54px;font-weight:300}
.hero-sub{position:absolute;left:0;right:0;top:114px;font-size:17px;font-weight:300}
.btn-outline{position:absolute;left:116px;top:163px;width:159px;height:30px;border:1px solid var(--white);color:var(--white)}

/* services */
.service{width:210px;text-align:center}
.service-icon{width:102px;height:102px;border-radius:50%;border:2px solid var(--teal);margin:0 auto;display:flex;align-items:center;justify-content:center;box-shadow:0 0 0 3px #e4f4f8}
.service-icon span{display:block;width:52px;height:52px;border-radius:50%;background:linear-gradient(135deg,#bfe8f2,#f3c9b0)}
.service h3{margin-top:26px;font-size:17px;font-weight:400;color:var(--ink)}
.service p{margin-top:9px;font-size:12px;line-height:18px}
.service a{display:block;margin-top:13px;font-size:12px;color:var(--teal);text-decoration:none}

/* about */
.about-bg{left:0;top:972px;width:1200px;height:461px;background:var(--pale)}
.about-photo-bg{left:0;top:972px;width:541px;height:461px;background:linear-gradient(135deg,#3cc2de,#1aa8c6 60%,#6fd0e4)}
.about-dots{left:541px;top:972px;width:20px;height:461px;background-image:radial-gradient(#d7dde0 1px,transparent 1.2px);background-size:5px 5px}
.about-portrait{left:280px;top:1012px;width:380px;height:380px;border-radius:50%;background:var(--white);box-shadow:0 4px 12px rgba(0,0,0,.2)}
.about-portrait span{position:absolute;left:14px;top:14px;width:352px;height:352px;border-radius:50%;background:linear-gradient(160deg,#5f8a4f,#7a5a48 55%,#2c2c33)}
.eyebrow{font-size:13px;color:var(--teal)}
.section-title{font-size:30px;font-weight:400;color:var(--ink)}
.about-copy{left:685px;top:1042px;width:370px}
.about-copy .section-title{margin-top:6px}
.about-copy p{margin-top:16px;font-size:12px;line-height:18px;color:var(--ink)}
.about-copy p+p{margin-top:10px}
.about-btn{margin-top:23px;width:98px;height:30px}

/* gallery */
.gallery-head{left:0;top:1506px;width:1200px;text-align:center}
.gallery-head .section-title{margin-top:4px}
.gallery-item{top:1593px;width:212px;height:203px;border:3px solid #e3e6e8}
.g1{left:151px;background:linear-gradient(135deg,#d8d6d1,#9c8f83)}
.g2{left:380px;background:linear-gradient(135deg,#e9e4dc,#8a7a6c)}
.g3{left:608px;background:linear-gradient(135deg,#c8b9a5,#5e7890)}
.g4{left:837px;background:linear-gradient(135deg,#cbb5a3,#8f7464)}
.gallery-btn{left:552px;top:1834px;width:96px;height:28px;font-size:11px}

/* contact */
.contact{left:0;top:1952px;width:1200px;height:469px;background:var(--teal)}
.contact-copy{left:149px;top:2000px;width:400px;color:var(--white)}
.contact-copy .eyebrow{color:var(--ink);font-weight:600;font-size:12px}
.contact-copy .section-title{color:var(--white);margin-top:2px}
.contact-copy p{margin-top:12px;font-size:12px;line-height:18px;width:380px}
.field{background:var(--white);height:35px;font-size:11px;color:#a2a8ad;padding:10px 12px}
.message{height:79px}
.send-btn{left:434px;top:2334px;width:97px;height:29px;background:#111;color:var(--white)}
.clinic-photo{left:627px;top:2099px;width:422px;height:254px;background:linear-gradient(180deg,#dfe8ee 0%,#6f8f5c 45%,#b4a48e 75%,#7e8d6a 100%)}

/* footer */
.site-footer{left:0;top:2421px;width:1200px;height:207px;background:var(--footer);text-align:center}
.footer-brand{position:absolute;left:0;right:0;top:38px;display:flex;justify-content:center;align-items:center;gap:8px}
.footer-brand .brand-name{width:auto;font-size:20px}
.social{position:absolute;left:0;right:0;top:118px;display:flex;justify-content:center;gap:13px}
.social span{width:25px;height:25px;border-radius:50%;background:#111}
.copyright{position:absolute;left:0;right:0;top:160px;font-size:10px;color:var(--ink)}
</style>
</head>
<body>

<header class="site-header abs">
  <div class="brand abs"><span class="brand-dot"></span><span class="brand-name">Brindle Oak Wellness Aftercare</span></div>
  <nav class="main-nav abs">
    <a class="active" href="#">HOME</a><span class="sep">|</span>
    <a href="#">SERVICES</a><span class="sep">|</span>
    <a href="#">FAQ</a><span class="sep">|</span>
    <a href="#">CONTACT US</a>
  </nav>
  <a class="btn btn-solid header-cta abs" href="#">Make an Appointment</a>
</header>

<section>
  <div class="hero-photo abs" role="img" aria-label="Hiker seated on a rock overlooking a fjord with snowy mountains"></div>
  <div class="hero-card abs">
    <h1 class="hero-title">Happiness</h1>
    <p class="hero-sub">There Are One Million Ways &nbsp;to Reach it!</p>
    <a class="btn btn-outline" href="#">Make an Appointment</a>
  </div>
</section>

<section>
  <div class="service abs" style="left:152px;top:639px">
    <div class="service-icon" role="img" aria-label="Head with brain icon"><span></span></div>
    <h3>Psychotherapy</h3>
    <p>Duis eget arcu et elit faucibus posuere in sit amet mi. Maecenas luctus dignissim luctus. Nullam rutrum ullamcorper quam a laoreet.</p>
    <a href="#">Know More</a>
  </div>
  <div class="service abs" style="left:380px;top:639px">
    <div class="service-icon" role="img" aria-label="Head with heart icon"><span></span></div>
    <h3>Grief &amp; Loss</h3>
    <p>Duis eget arcu et elit faucibus posuere in sit amet mi. Maecenas luctus dignissim luctus. Nullam rutrum ullamcorper quam a laoreet.</p>
    <a href="#">Know More</a>
  </div>
  <div class="service abs" style="left:610px;top:639px">
    <div class="service-icon" role="img" aria-label="Head with lightning icon"><span></span></div>
    <h3>Post-Traumatic</h3>
    <p>Duis eget arcu et elit faucibus posuere in sit amet mi. Maecenas luctus dignissim luctus. Nullam rutrum ullamcorper quam a laoreet.</p>
    <a href="#">Know More</a>
  </div>
  <div class="service abs" style="left:838px;top:639px">
    <div class="service-icon" role="img" aria-label="Head with clock icon"><span></span></div>
    <h3>Anxiety &amp; Worry</h3>
    <p>Duis eget arcu et elit faucibus posuere in sit amet mi. Maecenas luctus dignissim luctus. Nullam rutrum ullamcorper quam a laoreet.</p>
    <a href="#">Know More</a>
  </div>
</section>

<section>
  <div class="about-bg abs"></div>
  <div class="about-photo-bg abs" role="img" aria-label="Teal-tinted portrait of the therapist outdoors"></div>
  <div class="about-dots abs"></div>
  <div class="about-portrait abs"><span role="img" aria-label="Portrait of the lead therapist in front of greenery"></span></div>
  <div class="about-copy abs">
    <p class="eyebrow" style="margin:0;color:var(--teal);font-size:13px">About Us</p>
    <h2 class="section-title">Welcome to Brindle Oak</h2>
    <p>Maecenas elementum ac est at convallis. Curabitur orci quam, luctus at pharetra ac, dictum at diam. Mauris posuere turpis vel ligula convallis dapibus. Nullam pharetra, felis sed maximus lacinia, ligula turpis semper arcu, eu pretium eros libero id leo. Nam sagittis nibh at nulla egestas ullam-corper. Vestibulum quis quam erat.</p>
    <p>Maecenas non fermentum ligula, quis fermentum massa. Duis at eros dui. Orci varius natoque penatibus et magnis dis parturient montes, nascetur ridiculus mus. Nulla facilisi.</p>
    <a class="btn btn-solid about-btn" href="#">Learn More</a>
  </div>
</section>

<section>
  <div class="gallery-head abs">
    <p class="eyebrow">Pictures</p>
    <h2 class="section-title">Our Gallery</h2>
  </div>
  <div class="gallery-item g1 abs" role="img" aria-label="Therapist talking with a client on a sofa"></div>
  <div class="gallery-item g2 abs" role="img" aria-label="Young man in a session with a counsellor holding a clipboard"></div>
  <div class="gallery-item g3 abs" role="img" aria-label="Child in a play therapy session"></div>
  <div class="gallery-item g4 abs" role="img" aria-label="Hands held in comfort"></div>
  <a class="btn btn-solid gallery-btn abs" href="#">Explore More</a>
</section>

<section>
  <div class="contact abs"></div>
  <div class="contact-copy abs">
    <p class="eyebrow">Contact Us</p>
    <h2 class="section-title">Request Appointment</h2>
    <p>To request an appointment with Brindle Oak, please provide your contact information by filling out the form below</p>
  </div>
  <div class="field abs" style="left:149px;top:2141px;width:182px">Name</div>
  <div class="field abs" style="left:349px;top:2141px;width:182px">Phone No.</div>
  <div class="field abs" style="left:149px;top:2185px;width:182px">Email Id</div>
  <div class="field abs" style="left:349px;top:2185px;width:182px">Date</div>
  <div class="field message abs" style="left:149px;top:2230px;width:382px">Message</div>
  <a class="btn send-btn abs" href="#">Learn More</a>
  <div class="clinic-photo abs" role="img" aria-label="Clinic building with palm trees and a fountain"></div>
</section>

<footer class="site-footer abs">
  <div class="footer-brand"><span class="brand-dot"></span><span class="brand-name">Brindle Oak Wellness Aftercare</span></div>
  <div class="social"><span></span><span></span><span></span><span></span><span></span></div>
  <p class="copyright">©2019 By Brindle Oak. All Rights Reserved.</p>
</footer>

</body>
</html>
```